Professional Mothers Wordpress Site

*** To be clear, as a result of this contest I am looking for a fully functioning wordpress site to import into my wordpress site. Not just an image layout design.***

A Responsive Wordpress Blog Site for Professional Mothers

List of features desired:
1. Social media platform and commenting
2. Fully featured ecommerce store
3. Create and display fantastic-looking galleries of vimeo video content
4. Customised slideshows that are displayed in a content slider. Slides can be filled with text, images, video, social media stream feeds and syndicated content like Post feeds, Watch, Save, Flickr and more.
5. HTML5 and Flash compatible audio player that sits within the site. Works across both desktop and mobile devices
6. Admin panel
7. Google docs integrated email subscription, forms etc., email opt-in for newsletter
8. URL shortener
9. Enhanced image gallery
10. Interactive drag-and-drop pricing tables
11. Google Analytics, sitemaps
12. Rating system

List of pages on blogsite
1. Home page
2. About page
3. Resources page
4. Podcast archive page
5. Coaching page
6. Contact page

Here are some things I liked about the blogs I clicked through (and why I did or didn't like them)

Examples:
1) http://www.brindlepath.com/‎ - clean, professional feel
2) http://www.tessagrunwick.com/ - i like the simplicity of the email sign up and how it stands out without being obnoxious
3) http://velantrocast.com/ - i like the simplicity of the links to various pages at the top
4) http://www.quillsetworks.com/ - i like how the links are clear at the top and how they stay still even if the page moves (persistent headers)
5) http://www.makerstidehourly.com/ - i like how the podcast sessions are laid out on the front page
6) http://www.calvendo.com/ - this has a really nice 1st impression
7) http://uncleskiptrack.com/ - this has a nice layout too but the logo is way too big and it takes too long to scroll down to the content
8) http://zenbix.com/ - I like the moving content of this

Overall I'm going for something neat, clean and simple.

Target Market(s)

Working Mothers

Industry/Entity Type

Store

Requirements
Must have
• The social media links at the top of the page

```html
<!DOCTYPE html>
<html lang="en">
<head>
<meta charset="utf-8">
<title>Homeward Desk — Home</title>
<link href="https://fonts.googleapis.com/css2?family=Open+Sans:ital,wght@0,400;0,600;0,700;0,800;1,700;1,800&family=Oswald:wght@500&display=swap" rel="stylesheet">
<style>
:root{
  --purple:#98217d;
  --purple-dark:#7a1765;
  --ink:#222;
  --text:#555;
  --muted:#8a8a8a;
  --line:#dddddd;
  --page:#ececec;
  --panel:#ffffff;
  --black:#111;
  --orange:#f39a1e;
  --star:#e8a417;
  --blue-social:#3b5a97;
  --red-social:#c8232c;
  --grey-social:#6b6b6b;
  --sky-social:#3aa6e0;
}
*{box-sizing:border-box;margin:0;padding:0}
html,body{width:1200px;height:3702px;overflow:hidden}
body{background:var(--page);font-family:"Open Sans",Arial,sans-serif;color:var(--text);font-size:13px;position:relative}
a{color:inherit;text-decoration:none}

/* header */
.site-header{height:104px;background:#fff;border-bottom:3px solid var(--purple);position:relative}
.brand{position:absolute;left:140px;top:24px;display:flex;align-items:center;gap:10px}
.brand-mark{width:34px;height:34px;border-radius:50%;background:var(--purple)}
.brand-name{font-size:26px;font-weight:700;color:var(--purple);line-height:1}
.main-nav{position:absolute;left:392px;top:34px;display:flex;gap:0}
.main-nav a{font-size:15px;font-weight:700;color:#444;padding:4px 16px;letter-spacing:.5px}
.main-nav a.active{color:var(--purple);border-bottom:3px solid var(--purple)}

/* container */
.wrap{position:absolute;left:135px;top:114px;width:930px;height:3496px;background:var(--panel);box-shadow:0 0 14px rgba(0,0,0,.12)}

/* hero */
.hero{position:relative;height:435px;background:linear-gradient(120deg,#c9b8a3 0%,#e9d7c4 35%,#f3e7dc 60%,#b9a898 100%)}
.hero-card{position:absolute;left:16px;top:40px;width:300px;height:310px;background:rgba(255,255,255,.9);padding:18px}
.hero-card h1{font-family:"Oswald",sans-serif;font-weight:500;font-size:30px;line-height:1.05;color:#3a2a35;text-transform:uppercase;margin-bottom:14px}
.hero-card p{font-size:12px;line-height:1.55;color:#333;margin-bottom:14px}
.btn-purple{display:inline-block;background:var(--purple);color:#fff;font-weight:700;font-size:12px;padding:10px 14px;margin-top:12px}
.slider-arrows{position:absolute;left:440px;bottom:8px;display:flex;gap:4px}
.slider-arrows span{width:26px;height:26px;background:rgba(255,255,255,.75);display:flex;align-items:center;justify-content:center}

/* share buttons */
.share{display:flex;gap:6px}
.share span{display:flex;align-items:center;gap:3px;border:1px solid #ccc;border-radius:3px;background:#f7f7f7;font-size:10px;font-weight:600;color:#444;padding:2px 5px;height:20px}
.share span i{width:9px;height:9px;background:#999;display:inline-block}
.share span b{font-weight:400;color:#777;border-left:1px solid #ccc;padding-left:4px}

/* newsletter */
.newsletter{height:53px;background:var(--black);display:flex;align-items:center;padding-left:100px;position:relative}
.newsletter h2{color:#fff;font-style:italic;font-weight:800;font-size:17px;letter-spacing:.5px;margin-right:20px}
.newsletter .field{background:#fff;height:26px;width:196px;margin-right:8px;font-size:12px;color:#555;padding:4px 8px}
.got-it{position:absolute;left:780px;top:-4px;width:62px;height:62px;border-radius:50%;background:var(--orange);color:#fff;font-weight:800;font-style:italic;font-size:16px;display:flex;align-items:center;justify-content:center}

/* section headings */
.section-title{background:var(--purple);color:#fff;font-weight:800;font-size:15px;height:32px;line-height:32px;padding-left:8px;text-transform:uppercase}

/* video */
.videos{position:absolute;left:0;top:518px;width:930px}
.video-grid{display:flex;gap:12px;margin-top:9px}
.video-main{width:620px;height:346px;position:relative;background:linear-gradient(160deg,#8fc06b 0%,#b7d98c 40%,#e7dcc9 70%,#c8b39b 100%)}
.video-controls{position:absolute;left:0;right:0;bottom:0;height:30px;background:rgba(0,0,0,.7);display:flex;align-items:center;padding:0 10px;gap:10px;color:#fff;font-size:11px;font-weight:700}
.video-controls .bar{flex:1;height:4px;background:#666}
.video-thumbs{display:grid;grid-template-columns:143px 143px;grid-auto-rows:110px;gap:8px}
.thumb{background:linear-gradient(135deg,#e6d4c3,#c7a98e)}
.thumb.alt{background:linear-gradient(135deg,#b9d39a,#e7dccb)}

/* blog column */
.blogs{position:absolute;left:0;top:938px;width:664px}
.post{height:361px;border-bottom:1px solid var(--line);padding:20px 0 0 12px;position:relative}
.post-img{position:absolute;left:12px;top:20px;width:235px;height:220px;background:linear-gradient(150deg,#efdfcf,#c9a88c);display:flex;align-items:center;justify-content:center}
.post-img.green{background:linear-gradient(150deg,#bcd79c,#e8d8c4)}
.post-img.cool{background:linear-gradient(150deg,#dbe2ea,#b9a393)}
.post-body{position:absolute;left:268px;top:20px;width:384px}
.post-title{color:var(--purple);font-size:20px;font-weight:700;line-height:1.2;margin-bottom:6px}
.post-meta{font-size:11px;color:var(--muted);display:flex;gap:10px;align-items:center;margin-bottom:10px}
.stars{color:var(--star);letter-spacing:1px}
.stars em{color:#ccc;font-style:normal}
.post-excerpt{font-size:12px;line-height:1.6}
.post-foot{position:absolute;left:12px;right:12px;top:266px;display:flex;justify-content:space-between;align-items:center}
.btn-black{background:var(--black);color:#fff;font-weight:800;font-size:14px;padding:6px 12px;display:flex;align-items:center;gap:8px}
.btn-black svg{display:block}

/* sidebar */
.sidebar{position:absolute;left:683px;top:938px;width:247px}
.product{height:244px;padding:10px 0;border-bottom:1px solid var(--line)}
.product-img{width:218px;height:122px;background:linear-gradient(140deg,#ead8c6,#c6a58a);margin:0 auto 8px}
.product p{font-size:11px;line-height:1.45;color:#444}
.product-foot{display:flex;justify-content:space-between;align-items:flex-end;margin-top:6px}
.price{font-size:10px;color:#777}
.price strong{display:block;color:var(--purple);font-size:15px}
.buy{background:var(--black);color:#fff;font-weight:800;font-size:13px;padding:6px 10px}
.popular{margin-top:12px}
.popular ul{list-style:none;padding:10px 4px}
.popular li{color:var(--purple);font-size:12px;line-height:1.4;font-weight:600;margin-bottom:14px}
.social-card{height:293px;padding-top:12px;border-top:1px solid var(--line)}
.social-img{width:235px;height:120px;background:linear-gradient(140deg,#f0dcc5,#c7a68b);margin-bottom:8px}
.social-card p{font-size:11px;line-height:1.45;margin-bottom:8px}
.social-bar{height:52px;display:flex;justify-content:space-between;align-items:center;padding:0 10px;color:#fff}
.social-bar strong{display:block;font-size:12px}
.social-bar small{font-size:10px;opacity:.85}
.social-bar i{width:24px;height:24px;background:rgba(255,255,255,.9);display:block}
.s-blue{background:var(--blue-social)}.s-red{background:var(--red-social)}.s-grey{background:var(--grey-social)}.s-sky{background:var(--sky-social)}

/* footer */
.site-footer{position:absolute;left:0;top:3630px;width:1200px;height:72px;text-align:center;padding-top:14px}
.footer-nav{display:flex;justify-content:center;gap:26px;font-size:13px;font-weight:700;color:#333}
.footer-legal{margin-top:10px;font-size:11px;font-weight:600;color:#555}
</style>
</head>
<body>

<header class="site-header">
  <div class="brand"><span class="brand-mark"></span><span class="brand-name">Homeward Desk</span></div>
  <nav class="main-nav">
    <a class="active" href="#">HOME</a><a href="#">ABOUT</a><a href="#">RESOURCES</a><a href="#">PODCAST ARCHIVE</a><a href="#">COACHING</a><a href="#">CONTACT</a>
  </nav>
</header>

<main class="wrap">
  <section class="hero" role="img" aria-label="Photo of a smiling mother hugging her young child">
    <div class="hero-card">
      <h1>Lorem ipsum<br>dolor sit amet</h1>
      <p>Lorem ipsum dolor sit amet, consectetur adipisicing elit, sed do eiusmod tempor incididunt ut labore et dolore magna aliqua. Ut enim ad minim veniam, quis nostrud exercitation ullamco laboris nisi ut aliquip ex ea commodo consequat.</p>
      <div class="share"><span><i></i>Like <b>0</b></span><span><i></i>Post <b>0</b></span><span><i></i>Save <b>0</b></span></div>
      <a class="btn-purple" href="#">GET MORE DETAILS</a>
    </div>
    <div class="slider-arrows">
      <span><svg width="10" height="12" viewBox="0 0 10 12"><path d="M8 1 2 6l6 5" stroke="#333" stroke-width="2" fill="none"/></svg></span>
      <span><svg width="10" height="12" viewBox="0 0 10 12"><path d="M2 1l6 5-6 5" stroke="#333" stroke-width="2" fill="none"/></svg></span>
    </div>
  </section>

  <form class="newsletter">
    <h2>SIGNUP FOR NEWSLETTER</h2>
    <div class="field">First Name</div>
    <div class="field">E-Mail</div>
    <div class="got-it">Got it!</div>
  </form>

  <section class="videos">
    <h2 class="section-title">Video Galleries</h2>
    <div class="video-grid">
      <div class="video-main" role="img" aria-label="Video still of a mother lifting her baby above her on the grass">
        <div class="video-controls">
          <svg width="10" height="12" viewBox="0 0 10 12"><path d="M0 0l10 6-10 6z" fill="#fff"/></svg>
          <span class="bar"></span><span>HD</span>
          <svg width="14" height="12" viewBox="0 0 14 12"><rect x="1" y="1" width="12" height="10" fill="none" stroke="#fff" stroke-width="2"/></svg>
        </div>
      </div>
      <div class="video-thumbs">
        <div class="thumb" role="img" aria-label="Video thumbnail of a mother with children"></div>
        <div class="thumb alt" role="img" aria-label="Video thumbnail of a family outdoors"></div>
        <div class="thumb alt" role="img" aria-label="Video thumbnail of a mother reading with a child"></div>
        <div class="thumb" role="img" aria-label="Video thumbnail of a mother and baby"></div>
        <div class="thumb" role="img" aria-label="Video thumbnail of a mother kissing her child"></div>
        <div class="thumb alt" role="img" aria-label="Video thumbnail of a child playing"></div>
      </div>
    </div>
  </section>

  <section class="blogs">
    <h2 class="section-title">Blogs</h2>

    <article class="post">
      <div class="post-img" role="img" aria-label="Photo of a mother and daughter laughing together"></div>
      <div class="post-body">
        <h3 class="post-title">Lorem ipsum dolor sit amet, consectetur adipisicing elit.</h3>
        <div class="post-meta"><span>May 10, 2013</span><span>15</span><span>Rating <span class="stars">★★★<em>★★</em></span></span></div>
        <p class="post-excerpt">Sed ut perspiciatis unde omnis iste natus error sit voluptatem accusantium doloremque laudantium, totam rem aperiam, eaque ipsa quae ab illo inventore veritatis et quasi architecto beatae vitae dicta sunt explicabo. Nemo enim ipsam voluptatem quia voluptas sit aspernatur aut odit aut fugit, sed quia consequuntur magni dolores eos qui ratione voluptatem sequi nesciunt.</p>
      </div>
      <div class="post-foot">
        <div class="share"><span><i></i>Like <b>0</b></span><span><i></i>Post <b>0</b></span><span><i></i>Share <b>0</b></span><span><i></i>Save <b>0</b></span></div>
        <a class="btn-black" href="#">KEEP READING <svg width="12" height="12" viewBox="0 0 12 12"><path d="M3 1l6 5-6 5" stroke="#fff" stroke-width="2.5" fill="none"/></svg></a>
      </div>
    </article>

    <article class="post">
      <div class="post-img cool" role="img" aria-label="Video still of a mother holding her daughter"><svg width="54" height="54" viewBox="0 0 54 54"><circle cx="27" cy="27" r="26" fill="rgba(255,255,255,.85)"/><path d="M21 16l17 11-17 11z" fill="#333"/></svg></div>
      <div class="post-body">
        <h3 class="post-title">Lorem ipsum dolor sit amet, consectetur adipisicing elit.</h3>
        <div class="post-meta"><span>May 10, 2013</span><span>15</span><span>Rating <span class="stars">★★★<em>★★</em></span></span></div>
        <p class="post-excerpt">Sed ut perspiciatis unde omnis iste natus error sit voluptatem accusantium doloremque laudantium, totam rem aperiam, eaque ipsa quae ab illo inventore veritatis et quasi architecto beatae vitae dicta sunt explicabo. Nemo enim ipsam voluptatem quia voluptas sit aspernatur aut odit aut fugit, sed quia consequuntur magni dolores eos qui ratione voluptatem sequi nesciunt.</p>
      </div>
      <div class="post-foot">
        <div class="share"><span><i></i>Like <b>0</b></span><span><i></i>Post <b>0</b></span><span><i></i>Share <b>0</b></span><span><i></i>Save <b>0</b></span></div>
        <a class="btn-black" href="#">KEEP READING <svg width="12" height="12" viewBox="0 0 12 12"><path d="M3 1l6 5-6 5" stroke="#fff" stroke-width="2.5" fill="none"/></svg></a>
      </div>
    </article>

    <article class="post">
      <div class="post-img" role="img" aria-label="Photo of a mother hugging her young son"></div>
      <div class="post-body">
        <h3 class="post-title">Lorem ipsum dolor sit amet, consectetur adipisicing elit.</h3>
        <div class="post-meta"><span>May 10, 2013</span><span>15</span><span>Rating <span class="stars">★★★<em>★★</em></span></span></div>
        <p class="post-excerpt">Sed ut perspiciatis unde omnis iste natus error sit voluptatem accusantium doloremque laudantium, totam rem aperiam, eaque ipsa quae ab illo inventore veritatis et quasi architecto beatae vitae dicta sunt explicabo. Nemo enim ipsam voluptatem quia voluptas sit aspernatur aut odit aut fugit, sed quia consequuntur magni dolores eos qui ratione voluptatem sequi nesciunt.</p>
      </div>
      <div class="post-foot">
        <div class="share"><span><i></i>Like <b>0</b></span><span><i></i>Post <b>0</b></span><span><i></i>Share <b>0</b></span><span><i></i>Save <b>0</b></span></div>
        <a class="btn-black" href="#">KEEP READING <svg width="12" height="12" viewBox="0 0 12 12"><path d="M3 1l6 5-6 5" stroke="#fff" stroke-width="2.5" fill="none"/></svg></a>
      </div>
    </article>

    <article class="post">
      <div class="post-img green" role="img" aria-label="Photo of a mother lying on the grass with her baby"></div>
      <div class="post-body">
        <h3 class="post-title">Lorem ipsum dolor sit amet, consectetur adipisicing elit.</h3>
        <div class="post-meta"><span>May 10, 2013</span><span>15</span><span>Rating <span class="stars">★★★<em>★★</em></span></span></div>
        <p class="post-excerpt">Sed ut perspiciatis unde omnis iste natus error sit voluptatem accusantium doloremque laudantium, totam rem aperiam, eaque ipsa quae ab illo inventore veritatis et quasi architecto beatae vitae dicta sunt explicabo. Nemo enim ipsam voluptatem quia voluptas sit aspernatur aut odit aut fugit, sed quia consequuntur magni dolores eos qui ratione voluptatem sequi nesciunt.</p>
      </div>
      <div class="post-foot">
        <div class="share"><span><i></i>Like <b>0</b></span><span><i></i>Post <b>0</b></span><span><i></i>Share <b>0</b></span><span><i></i>Save <b>0</b></span></div>
        <a class="btn-black" href="#">KEEP READING <svg width="12" height="12" viewBox="0 0 12 12"><path d="M3 1l6 5-6 5" stroke="#fff" stroke-width="2.5" fill="none"/></svg></a>
      </div>
    </article>

    <article class="post">
      <div class="post-img cool" role="img" aria-label="Video still of a mother and child outdoors"><svg width="54" height="54" viewBox="0 0 54 54"><circle cx="27" cy="27" r="26" fill="rgba(255,255,255,.85)"/><path d="M21 16l17 11-17 11z" fill="#333"/></svg></div>
      <div class="post-body">
        <h3 class="post-title">Lorem ipsum dolor sit amet, consectetur adipisicing elit.</h3>
        <div class="post-meta"><span>May 10, 2013</span><span>15</span><span>Rating <span class="stars">★★★<em>★★</em></span></span></div>
        <p class="post-excerpt">Sed ut perspiciatis unde omnis iste natus error sit voluptatem accusantium doloremque laudantium, totam rem aperiam, eaque ipsa quae ab illo inventore veritatis et quasi architecto beatae vitae dicta sunt explicabo. Nemo enim ipsam voluptatem quia voluptas sit aspernatur aut odit aut fugit, sed quia consequuntur magni dolores eos qui ratione voluptatem sequi nesciunt.</p>
      </div>
      <div class="post-foot">
        <div class="share"><span><i></i>Like <b>0</b></span><span><i></i>Post <b>0</b></span><span><i></i>Share <b>0</b></span><span><i></i>Save <b>0</b></span></div>
        <a class="btn-black" href="#">KEEP READING <svg width="12" height="12" viewBox="0 0 12 12"><path d="M3 1l6 5-6 5" stroke="#fff" stroke-width="2.5" fill="none"/></svg></a>
      </div>
    </article>

    <article class="post">
      <div class="post-img green" role="img" aria-label="Video still of a mother and son in a garden"><svg width="54" height="54" viewBox="0 0 54 54"><circle cx="27" cy="27" r="26" fill="rgba(255,255,255,.85)"/><path d="M21 16l17 11-17 11z" fill="#333"/></svg></div>
      <div class="post-body">
        <h3 class="post-title">Lorem ipsum dolor sit amet, consectetur adipisicing elit.</h3>
        <div class="post-meta"><span>May 10, 2013</span><span>15</span><span>Rating <span class="stars">★★★<em>★★</em></span></span></div>
        <p class="post-excerpt">Sed ut perspiciatis unde omnis iste natus error sit voluptatem accusantium doloremque laudantium, totam rem aperiam, eaque ipsa quae ab illo inventore veritatis et quasi architecto beatae vitae dicta sunt explicabo. Nemo enim ipsam voluptatem quia voluptas sit aspernatur aut odit aut fugit, sed quia consequuntur magni dolores eos qui ratione voluptatem sequi nesciunt.</p>
      </div>
      <div class="post-foot">
        <div class="share"><span><i></i>Like <b>0</b></span><span><i></i>Post <b>0</b></span><span><i></i>Share <b>0</b></span><span><i></i>Save <b>0</b></span></div>
        <a class="btn-black" href="#">KEEP READING <svg width="12" height="12" viewBox="0 0 12 12"><path d="M3 1l6 5-6 5" stroke="#fff" stroke-width="2.5" fill="none"/></svg></a>
      </div>
    </article>

    <article class="post" style="border-bottom:0">
      <div class="post-img cool" role="img" aria-label="Photo of a mother holding her baby in a bright room"></div>
      <div class="post-body">
        <h3 class="post-title">Lorem ipsum dolor sit amet, consectetur adipisicing elit.</h3>
        <div class="post-meta"><span>May 10, 2013</span><span>15</span><span>Rating <span class="stars">★★★<em>★★</em></span></span></div>
        <p class="post-excerpt">Sed ut perspiciatis unde omnis iste natus error sit voluptatem accusantium doloremque laudantium, totam rem aperiam, eaque ipsa quae ab illo inventore veritatis et quasi architecto beatae vitae dicta sunt explicabo. Nemo enim ipsam voluptatem quia voluptas sit aspernatur aut odit aut fugit, sed quia consequuntur magni dolores eos qui ratione voluptatem sequi nesciunt.</p>
      </div>
      <div class="post-foot">
        <div class="share"><span><i></i>Like <b>0</b></span><span><i></i>Post <b>0</b></span><span><i></i>Share <b>0</b></span><span><i></i>Save <b>0</b></span></div>
        <a class="btn-black" href="#">KEEP READING <svg width="12" height="12" viewBox="0 0 12 12"><path d="M3 1l6 5-6 5" stroke="#fff" stroke-width="2.5" fill="none"/></svg></a>
      </div>
    </article>
  </section>

  <aside class="sidebar">
    <h2 class="section-title">Ecommerce Store</h2>
    <div class="product">
      <div class="product-img" role="img" aria-label="Product photo of a mother with her child"></div>
      <p>Lorem ipsum dolor sit amet, consectetur adipiscing elit</p>
      <div class="product-foot"><div class="price">Price<strong>$50.00</strong></div><a class="buy" href="#">BUY NOW</a></div>
    </div>
    <div class="product">
      <div class="product-img" role="img" aria-label="Product photo of a mother and daughter"></div>
      <p>Lorem ipsum dolor sit amet, consectetur adipiscing elit</p>
      <div class="product-foot"><div class="price">Price<strong>$50.00</strong></div><a class="buy" href="#">BUY NOW</a></div>
    </div>
    <div class="product" style="border-bottom:0">
      <div class="product-img" role="img" aria-label="Product photo of a mother kissing her baby"></div>
      <p>Lorem ipsum dolor sit amet, consectetur adipiscing elit</p>
      <div class="product-foot"><div class="price">Price<strong>$50.00</strong></div><a class="buy" href="#">BUY NOW</a></div>
    </div>

    <section class="popular">
      <h2 class="section-title">Most Popular</h2>
      <ul>
        <li>Proin id ligula id mauris luctus aliquam nec a litora.</li>
        <li>Morbi aliquet odio ut libero rutrum sagittis.</li>
        <li>Nulla sed mi dapibus lacus interdum vulputate.</li>
        <li>Phasellus nec lacus a felis venenatis eleifend.</li>
        <li>Morbi aliquet odio ut libero rutrum sagittis.</li>
        <li>Phasellus sed lacus a dapibus lacus eleifend.</li>
      </ul>
    </section>

    <div class="social-card">
      <div class="social-img" role="img" aria-label="Photo of a family sitting together"></div>
      <p>Sed ut perspiciatis unde omnis iste natus error sit voluptatem accusantium doloremque laudantium, totam rem aperiam.</p>
      <div class="social-bar s-blue"><div><strong>Lorem ipsum dolor</strong><small>1 days ago</small></div><i></i></div>
    </div>
    <div class="social-card">
      <div class="social-img" role="img" aria-label="Photo of a mother and daughter in sunlight"></div>
      <p>Sed ut perspiciatis unde omnis iste natus error sit voluptatem accusantium doloremque laudantium, totam rem aperiam.</p>
      <div class="social-bar s-red"><div><strong>Lorem ipsum dolor</strong><small>1 days ago</small></div><i></i></div>
    </div>
    <div class="social-card">
      <div class="social-img" role="img" aria-label="Photo of a mother working on a laptop with her child"></div>
      <p>Sed ut perspiciatis unde omnis iste natus error sit voluptatem accusantium doloremque laudantium, totam rem aperiam.</p>
      <div class="social-bar s-grey"><div><strong>Lorem ipsum dolor</strong><small>1 days ago</small></div><i></i></div>
    </div>
    <div class="social-card">
      <div class="social-img" role="img" aria-label="Photo of a mother hugging her toddler"></div>
      <p>Sed ut perspiciatis unde omnis iste natus error sit voluptatem accusantium doloremque laudantium, totam rem aperiam.</p>
      <div class="social-bar s-sky"><div><strong>Lorem ipsum dolor</strong><small>1 days ago</small></div><i></i></div>
    </div>
  </aside>
</main>

<footer class="site-footer">
  <nav class="footer-nav"><a href="#">HOME</a><a href="#">ABOUT</a><a href="#">RESOURCES</a><a href="#">PODCAST ARCHIVE</a><a href="#">COACHING</a><a href="#">CONTACT</a></nav>
  <p class="footer-legal">PRIVACY POLICY &nbsp;|&nbsp; © 2013 HOMEWARD DESK &nbsp;|&nbsp; TERMS POLICY &nbsp;|&nbsp; DISCLAIMER</p>
</footer>

</body>
</html>
```